KB Sports & Remedial Massage needs a new logo & business card design

The design is for my Sports and remedial massage business. My business is aimed at everyone who has a muscle ache or injury so not just sports related. I need a design which is sharp, clear and professional. No greens, or pastel colours or floral/girly designs. Perhaps just a Navy background and white text or other way around or perhaps grey. I want to make it clear that I treat everyone and not just sporty people.

Target Market(s)

People with muscle aches or sports injuries

Industry/Entity Type

Health And Wellness

Contact Information for Business Card

It needs to also include the following:
Name: Megan Hartwell
Mobile No: 07493 215 648
Email: meganhartwell@parcelnet.example
Qualifications: Dip SM, Dip SRM

Logo Text

KB Sports & Remedial Massage

Font styles to use
Serif
Other font styles liked:
• Tahoma, Verdana

Colors
5c5c5c
7f7f7f
9d9d9d
0255a3
3176b5
85abd2

Requirements
Must have
• I was thinking of a few simple people figures at the bottom of the card to highlight this i.e. a gardener, musician mixed in with a cyclist and tennis player.
Should not have
• Anything which indicates beauty therapy or relaxing. I am there to get rid of aches and pains and often to give rehab to certain injuries.

```html
<!DOCTYPE html>
<html lang="en">
<head>
<meta charset="utf-8">
<title>KB Sports &amp; Remedial Massage – Business Cards</title>
<link href="https://fonts.googleapis.com/css2?family=Open+Sans:wght@400;700;800&display=swap" rel="stylesheet">
<style>
  :root {
    --page-bg: #ecebe8;
    --white: #ffffff;
    --charcoal: #2b2a2a;
    --signal-red: #e30613;
    --navy: #253a6d;
    --steel-grey: #9d9d9d;
    --figure-grey: #8a8a8a;
    --figure-navy: #6a7ba3;
  }
  html, body {
    margin: 0;
    width: 1200px;
    height: 995px;
    overflow: hidden;
    background: var(--page-bg);
    font-family: "Open Sans", Verdana, sans-serif;
  }
  .card {
    position: absolute;
    top: 118px;
    width: 432px;
    height: 720px;
    background: var(--white);
    box-shadow: 0 2px 6px rgba(0,0,0,.18);
    overflow: hidden;
  }
  .card--red { left: 80px; --accent: var(--signal-red); --sweep: var(--charcoal); --panel: var(--charcoal); --brand: var(--charcoal); --figures: var(--figure-grey); --art: #3a3a3a; }
  .card--navy { left: 634px; --accent: var(--navy); --sweep: var(--steel-grey); --panel: var(--navy); --brand: var(--navy); --figures: var(--figure-navy); --art: #8f8f8f; }

  .card__sweep { position: absolute; top: 0; left: 0; width: 432px; height: 90px; }
  .card__sweep .sweep-accent { fill: var(--accent); }
  .card__sweep .sweep-band { fill: var(--sweep); }

  .card__illustration {
    position: absolute;
    top: 40px;
    left: 70px;
    width: 240px;
    height: 255px;
    border-radius: 8px;
    background: radial-gradient(ellipse at 55% 45%, var(--art) 0%, rgba(255,255,255,0) 72%);
    opacity: .35;
  }

  .brand-name {
    position: absolute;
    top: 322px;
    left: 0;
    width: 432px;
    text-align: center;
    margin: 0;
    font-weight: 800;
    font-size: 25px;
    line-height: 32px;
    color: var(--brand);
    text-transform: uppercase;
  }
  .brand-name__line { display: block; }
  .brand-name__line--spaced { letter-spacing: 9px; padding-left: 9px; }

  .card__divider {
    position: absolute;
    top: 406px;
    left: 0;
    width: 432px;
    height: 8px;
    background: var(--accent);
  }
  .card--navy .card__divider { background: var(--steel-grey); }

  .card__contact {
    position: absolute;
    top: 414px;
    left: 0;
    width: 432px;
    height: 306px;
    background: var(--panel);
    color: var(--white);
  }
  .contact__name { position: absolute; top: 34px; left: 55px; margin: 0; font-size: 23px; font-weight: 700; }
  .contact__quals { position: absolute; top: 70px; left: 55px; margin: 0; font-size: 17px; }
  .contact__line { position: absolute; left: 55px; margin: 0; font-size: 19px; display: flex; align-items: center; gap: 8px; }
  .contact__line--phone { top: 112px; }
  .contact__line--email { top: 149px; }
  .contact__icon { width: 20px; height: 20px; fill: none; stroke: var(--accent); stroke-width: 1.8; }
  .card--navy .contact__icon { stroke: var(--white); }

  .contact__figures {
    position: absolute;
    top: 192px;
    left: 42px;
    width: 340px;
    height: 96px;
    border-radius: 6px;
    background: linear-gradient(90deg, var(--figures), rgba(255,255,255,.12) 50%, var(--figures));
    opacity: .55;
  }
</style>
</head>
<body>

<section class="card card--red">
  <svg class="card__sweep" viewBox="0 0 432 90" aria-hidden="true">
    <path class="sweep-accent" d="M0 0H250C150 10 60 40 0 80Z"/>
    <path class="sweep-band" d="M105 34C200 8 320 2 432 2V30C330 14 220 18 105 34Z"/>
  </svg>
  <div class="card__illustration" role="img" aria-label="Line drawing of a person's back with pain points on the shoulder, neck and lower back"></div>
  <h1 class="brand-name"><span class="brand-name__line">KB Sports &amp; Remedial</span><span class="brand-name__line brand-name__line--spaced">Massage</span></h1>
  <div class="card__divider"></div>
  <div class="card__contact">
    <p class="contact__name">Megan Hartwell</p>
    <p class="contact__quals">Qualifications: Dip SM, Dip SRM</p>
    <p class="contact__line contact__line--phone">
      <svg class="contact__icon" viewBox="0 0 20 20" aria-hidden="true"><rect x="5" y="2" width="10" height="16" rx="2"/><line x1="9" y1="15" x2="11" y2="15"/></svg>
      07493 215 648
    </p>
    <p class="contact__line contact__line--email">
      <svg class="contact__icon" viewBox="0 0 20 20" aria-hidden="true"><rect x="2" y="5" width="16" height="11"/><path d="M2 5l8 6 8-6"/></svg>
      meganhartwell@parcelnet.example
    </p>
    <div class="contact__figures" role="img" aria-label="Silhouettes of a gardener with a lawnmower, a guitarist, a cyclist and a tennis player"></div>
  </div>
</section>

<section class="card card--navy">
  <svg class="card__sweep" viewBox="0 0 432 90" aria-hidden="true">
    <path class="sweep-accent" d="M0 0H250C150 10 60 40 0 80Z"/>
    <path class="sweep-band" d="M105 34C200 8 320 2 432 2V30C330 14 220 18 105 34Z"/>
  </svg>
  <div class="card__illustration" role="img" aria-label="Line drawing of a person's back with pain points on the shoulder, neck and lower back"></div>
  <h1 class="brand-name"><span class="brand-name__line">KB Sports &amp; Remedial</span><span class="brand-name__line brand-name__line--spaced">Massage</span></h1>
  <div class="card__divider"></div>
  <div class="card__contact">
    <p class="contact__name">Megan Hartwell</p>
    <p class="contact__quals">Qualifications: Dip SM, Dip SRM</p>
    <p class="contact__line contact__line--phone">
      <svg class="contact__icon" viewBox="0 0 20 20" aria-hidden="true"><rect x="5" y="2" width="10" height="16" rx="2"/><line x1="9" y1="15" x2="11" y2="15"/></svg>
      07493 215 648
    </p>
    <p class="contact__line contact__line--email">
      <svg class="contact__icon" viewBox="0 0 20 20" aria-hidden="true"><rect x="2" y="5" width="16" height="11"/><path d="M2 5l8 6 8-6"/></svg>
      meganhartwell@parcelnet.example
    </p>
    <div class="contact__figures" role="img" aria-label="Silhouettes of a gardener with a lawnmower, a guitarist, a cyclist and a tennis player"></div>
  </div>
</section>

</body>
</html>
```